Geschäftspapiere für Termin Startup
Zielgruppe
Wir sind ein Startup, das über die Seite Planorix.de (derzeit noch in der Beta-Phase)zukünftig folgenden Service anbietet: Unternehmer können sehr flexibel (selbst) gestaltete Terminformulare erstellen und auf Ihrer Website einbinden. Kunden können dann diese Termine buchen und bekommen dann Erinnerungs-Mails und SMS.
Zielgruppe: Dienstleister wie Fotografen, Friseure, Versicherungsvertreter, Masseure, Restaurants, Arztpraxen. Also alle, die darauf angewiesen sind, dass vereinbarte Termine eingehalten werden und die die Terminvereinbarung vereinfachen wollen. Also weniger per Telefon, mehr über die eigene Website.
Dateien bitte beachten für die Ansicht des Look & Feels:
https://ablage.beispielwolke.de/open?id=7QmrtHkWz2LpA94bNc3sVyTeOx8dGJuR_
Bonus-Aktion: Wir zahlen pauschal jeweils 30,00 Euro an die Designer auf den Plätzen 2 bis 4 für die geleistete Arbeit. Nur einer kann gewinnen und den Zuschlag bekommen. Aber so möchten wir gerne die Arbeit dennoch honorieren.
Aufgabenstellung
Wir benötigen ein modernes Briefpapier-Layout passend zu unserem CD.
Gerne darf/soll der ORBO (siehe Maskottchen in https://ablage.beispielwolke.de/open?id=5PwqNsYt8BaLmr2Hc7xkDuQOEPfjWzVbn )darauf erscheinen.
Maskottchen ORBO gibt es in mehreren Varianten. Siehe https://ablage.beispielwolke.de/ordner/8TrnWqLeHd5XcmZ3sJ4yPvBkGfQaNuRox?teilen=ja
Auch als Variante, das Maskottchen ORBO gegen das Logo gelehnt ist, kann genutzt werden: https://ablage.beispielwolke.de/open?id=3MuxBgTpW7RkaNj6yVqLeDsHcZoPfGtYi
Das Thema 'Terminvereinbarung' soll sofort erfasst werden mittels des Layouts bzw. der grafischen Elemente.
Auch die Branchen-Icons ( https://ablage.beispielwolke.de/ordner/6HpvRtNmQ2WkzLx8yEcBaJdFsUoGiTbeq?teilen=ja ) dürfen verwendet werden.

```html
<!DOCTYPE html>
<html lang="de">
<head>
<meta charset="utf-8">
<title>Planorix Briefpapier</title>
<link href="https://fonts.googleapis.com/css2?family=Cabin:wght@400;600;700&display=swap" rel="stylesheet">
<style>
  :root{
    --green:#8cc63e;
    --red:#e2312d;
    --yellow:#f6b91b;
    --ink:#5d646b;
    --ink-soft:#6f767d;
    --footer:#868d94;
    --paper:#ffffff;
  }
  *{margin:0;padding:0;box-sizing:border-box}
  html,body{width:848px;height:1200px;overflow:hidden;background:var(--paper)}
  body{font-family:"Cabin",sans-serif;color:var(--ink);position:relative}
  .letter{position:relative;width:848px;height:1200px;overflow:hidden}

  .header-rule{position:absolute;top:77px;height:2px;background:var(--green)}
  .header-rule.left{left:0;width:283px}
  .header-rule.right{left:592px;width:256px}

  .brand{position:absolute;left:293px;top:46px;width:296px;height:70px}
  .brand-mark{position:absolute;left:0;top:18px;width:30px;height:30px;background:var(--ink-soft);border-radius:3px}
  .brand-name{position:absolute;left:42px;top:6px;font-size:44px;font-weight:700;color:var(--green);line-height:1;letter-spacing:-0.5px;white-space:nowrap}
  .brand-tag{position:absolute;left:166px;top:50px;font-size:12px;color:var(--ink-soft);white-space:nowrap}

  .sender-line{position:absolute;left:101px;top:173px;font-size:10.5px;color:var(--ink);white-space:nowrap}
  .sender-line b{font-weight:700}

  .recipient{position:absolute;left:101px;top:200px;font-size:13.6px;line-height:18.6px}

  .contact{position:absolute;left:505px;top:200px;font-size:13.6px;line-height:18.6px}
  .contact b{font-weight:700}
  .contact p{margin-bottom:12px}

  .subject{position:absolute;left:101px;top:392px;font-size:16px;font-weight:700}

  .body{position:absolute;left:101px;top:457px;width:628px;font-size:13.2px;line-height:19.7px;text-align:justify;hyphens:auto}
  .body p{margin-bottom:9px}
  .body .greeting{margin-bottom:11px}
  .closing{margin-top:8px}
  .signature{display:block;width:60px;height:22px;margin:2px 0 4px;background:linear-gradient(90deg,#2b2b2b22,#2b2b2b10);border-radius:3px}
  .signer{font-size:9.5px;line-height:13px}

  .mascot{position:absolute;left:577px;top:862px;width:271px;height:216px;
    background:radial-gradient(ellipse at 60% 40%,#8cc63e 0%,#b9c0c6 55%,rgba(255,255,255,0) 75%)}

  .footer-strip{position:absolute;top:1078px;height:4px}
  .footer-strip.green{left:0;width:342px;background:var(--green)}
  .footer-strip.red{left:342px;width:222px;background:var(--red)}
  .footer-strip.yellow{left:564px;width:284px;background:var(--yellow)}
  .footer{position:absolute;left:0;top:1082px;width:848px;height:118px;background:var(--footer);color:#fff}
  .footer-col{position:absolute;top:16px;font-size:10px;line-height:15.5px;white-space:nowrap}
  .footer-col b{font-weight:700}
</style>
</head>
<body>
<div class="letter">
  <div class="header-rule left"></div>
  <div class="header-rule right"></div>
  <div class="brand">
    <div class="brand-mark"></div>
    <div class="brand-name">Planorix</div>
    <div class="brand-tag">Tool by termwerk-app.com</div>
  </div>

  <div class="sender-line"><b>Planorix GmbH</b> | Musterstraße 23 | 12345 Musterhausen</div>

  <div class="recipient">
    Friseursalon Lockenwerk<br>
    Frau Jana Wellner<br>
    Lindenhof 9<br>
    10117 Berlin
  </div>

  <div class="contact">
    <p><b>Ansprechpartner:</b> Konstantin Berger</p>
    <p><b>Abteilung:</b> Kundenservice</p>
    <p><b>Telefon:</b> 04567 - 21 94 30 -12<br>
       <b>Telefax:</b> 04567 - 21 94 30 -134<br>
       <b>E-Mail:</b>&nbsp; k.berger@planorix.de</p>
    <p><b>Datum:</b>&nbsp; 24. Juni 2018</p>
  </div>

  <div class="subject">Betreffzeile Lorem ipsum dolor sit amet</div>

  <div class="body">
    <p class="greeting">Sehr geehrte Frau Wellner,</p>
    <p>lorem ipsum dolor sit amet, consetetur sadipscing elitr, sed diam nonumy eirmod tempor invidunt ut labore et dolore magna aliquyam erat, sed diam voluptua. At vero eos et accusam et justo duo dolores et ea rebum. Stet clita kasd gubergren, no sea takimata sanctus est Lorem ipsum dolor sit amet. Lorem ipsum dolor sit amet, consetetur sadipscing elitr, sed diam nonumy eirmod tempor invidunt ut labore et dolore magna aliquyam erat, sed diam voluptua. At vero eos et accusam et justo duo dolores et ea rebum. Stet clita kasd gubergren, no sea takimata sanctus est Lorem ipsum dolor sit amet. Lorem ipsum dolor sit amet, consetetur sadipscing elitr, sed diam nonumy eirmod tempor invidunt ut labore et dolore magna aliquyam erat, sed diam voluptua. At vero eos et accusam et justo duo dolores et ea rebum. Stet clita kasd gubergren, no sea takimata sanctus est Lorem ipsum dolor sit amet.</p>
    <p>Duis autem vel eum iriure dolor in hendrerit in vulputate velit esse molestie consequat, vel illum dolore eu feugiat nulla facilisis at vero eros et accumsan et iusto odio dignissim qui blandit praesent luptatum zzril delenit augue duis dolore te feugait nulla facilisi. Lorem ipsum dolor sit amet, consectetuer adipiscing elit, sed diam nonummy nibh euismod tincidunt ut laoreet dolore magna aliquam erat volutpat.</p>
    <p>Ut wisi enim ad minim veniam, quis nostrud exerci tation ullamcorper suscipit lobortis nisl ut aliquip ex ea commodo consequat. Duis autem vel eum iriure dolor in hendrerit in vulputate velit esse molestie consequat, vel illum dolore eu feugiat nulla facilisis at vero eros et accumsan et iusto odio dignissim qui blandit praesent luptatum zzril delenit augue duis dolore te feugait nulla facilisi.</p>
    <p class="closing">Mit freundlichen Grüßen,</p>
    <span class="signature" role="img" aria-label="Handschriftliche Unterschrift"></span>
    <div class="signer">Konstantin Berger<br>Projektmanager</div>
  </div>

  <div class="mascot" role="img" aria-label="Platz für die Maskottchen-Illustration"></div>

  <div class="footer-strip green"></div>
  <div class="footer-strip red"></div>
  <div class="footer-strip yellow"></div>
  <div class="footer">
    <div class="footer-col" style="left:101px"><b>Planorix GmbH</b><br>Musterstraße 23<br>12345 Musterhausen</div>
    <div class="footer-col" style="left:226px">Geschäftsführer: Henrik Saalfeld<br>Handelsregister Musterhausen<br>Musterhausener Bank<br>IBAN: DE48 7003 1122 4590 87<br>BIC: KOVRDEX21PL</div>
    <div class="footer-col" style="left:414px"><b>Bankverbindung</b><br>IBAN: DE48 7003 1122 4590 87<br>BIC: KOVRDEX21PL<br>USt-IdNr: DE31740582</div>
    <div class="footer-col" style="left:594px"><b>Kontakt</b><br>Telefon: 04567 - 21 94 30 0<br>Telefax: 04567 - 21 94 30 - 134<br>E-Mail: info@planorix.de<br>Webseite: www.planorix.de</div>
  </div>
</div>
</body>
</html>
```